LoomPages app needs an improved design

LoomPages makes available books that have been banned in certain countries. The current version of the app is available for download here: https://apps.quillmarket.example/details?id=org.tallbrook.loompage

At the moment, the app is available only in Chinese. Books are made available within the app, in text or audio format. Books can be downloaded for offline use. We created the app as a way to circumvent the intense censorship that is placed on book distribution inside China. The app is designed in such a way that the authorities are not able to censor the app, thus users in China are able to download the app, read content and receive updates to the app. So far over 100,000 people have used the app. Books are made available to the users for free and the app is also free to download.

We have used a similar anti-censorship strategy in a number of other apps, all with equally successful outcomes.

The app is only available on Android. While many Chinese purchase high end Android devices, Android is also the operating system of choice for new internet users in China. Oftentimes, the first time a user accesses the internet will be through an inexpensive Android smartphone.

This is very much a content driven app, with limited functionality but very visual. We need to optimize the app so that it is suitable for reading long texts. While we make available banned books through the app itself, our users are primarily avid readers - they are not likely to be netizens who wanted to download a book app just because it contains banned books. They will be readers who are interested in reading and exploring new books that are not normally available to them.

The app should have similar functionality to an e-reader, like a Vessly, however it needs to be optimized for smaller screens. Apps like Tornwick present content in an easy to read format.

Target Market(s)

Our current end users are Chinese who are professionals and have an interest in reading. They are likely between the ages of 18-50. We try to make the app as easy and intuitive as possible. Even though there are over 700 million people online in China, another 600 million of them will come online soon. We want experienced internet and technology users to easily find the content they are looking for and we want new internet and technology users to be able to easily use the app. Our users mainly use the app in the comfort of their own home - as they would read an e-book (Vessly) or in a quiet cafe.

Industry/Entity Type

Book Publisher

Font styles to use
Serif

Colors

Designer to choose colors to be used in the design.

Requirements
Must have
• Our current challenges include:
• - We want to promote new books as well as popular books (and potentially other categories) and allow users to browse more books in that category.
• - Allow users to search.
• - For each book, we need an indication whether it is an audio book or a text book.
• - For each book, we need an indication whether the book has already been downloaded.
• Our current audio book challenges include:
• - Show book cover.
• - Include all standard audio playback functions (pause, play, next chapter etc).
• - Audio books can play in the background. When the user leaves this view, the app needs to indicate that an audio book is playing in the background, and show the user how to return to this interface (to pause playback, etc).
• Our current text book challenges include:
• - Show name of book.
• - Maximize use of screen (since it may be hard to read on a small device).
• - Allow user to easily navigate (next page, any page number etc).

```html
<!DOCTYPE html>
<html lang="en">
<head>
<meta charset="utf-8">
<title>LoomPages — Reader Screens</title>
<link rel="stylesheet" href="https://fonts.googleapis.com/css2?family=DM+Serif+Display&family=Cormorant+Garamond:wght@400&family=Roboto:wght@400&display=swap">
<style>
  :root {
    --stage-top: #e9eef2;
    --stage-bottom: #f3f5f7;
    --paper: #ffffff;
    --ink: #2a2a2a;
    --body-text: #858585;
    --icon-dark: #5a5a5a;
    --control-grey: #dcdcdc;
    --on-photo: #ffffff;
    --sky-top: #d8d2cf;
    --sky-mid: #b9b7bb;
    --sea: #5f7880;
    --deep: #33474c;
    --pill: rgba(200, 205, 208, 0.55);
    --pill-text: #3f4548;
  }
  * { box-sizing: border-box; margin: 0; padding: 0; }
  html, body { width: 1200px; height: 827px; overflow: hidden; }
  body {
    position: relative;
    background: radial-gradient(ellipse at 50% 40%, var(--stage-bottom) 0%, var(--stage-top) 100%);
    font-family: "Roboto", sans-serif;
  }
  .screen {
    position: absolute;
    top: 82px;
    width: 388px;
    height: 645px;
    box-shadow: 0 18px 40px rgba(90, 110, 125, 0.22);
    overflow: hidden;
  }
  .screen--cover { left: 146px; }
  .screen--chapter { left: 665px; background: var(--paper); }

  .cover-photo {
    position: absolute; inset: 0;
    background:
      linear-gradient(90deg, rgba(40,55,60,0.55) 0%, rgba(40,55,60,0.15) 45%, rgba(0,0,0,0) 70%),
      linear-gradient(180deg, var(--sky-top) 0%, var(--sky-mid) 45%, var(--sea) 75%, var(--deep) 100%);
  }
  .icon { position: absolute; display: block; }
  .cover-menu { left: 32px; top: 28px; }
  .cover-sound { left: 340px; top: 26px; }

  .cover-text { position: absolute; left: 34px; top: 314px; color: var(--on-photo); }
  .cover-author {
    font-family: "Cormorant Garamond", serif;
    font-size: 21px; line-height: 26px; font-weight: 400;
    opacity: 0.92; margin-bottom: 10px;
  }
  .cover-title {
    font-family: "DM Serif Display", serif;
    font-weight: 400; font-size: 35px; line-height: 40px;
    letter-spacing: -0.3px;
  }
  .read-button {
    display: block;
    position: absolute; left: 34px; top: 491px;
    width: 97px; height: 22px; border: 0; border-radius: 11px;
    background: var(--pill); color: var(--pill-text);
    font-family: "Roboto", sans-serif; font-size: 9px; letter-spacing: 1.5px;
  }

  .chapter-menu { left: 31px; top: 22px; }
  .chapter-next { left: 338px; top: 22px; }
  .chapter-title {
    position: absolute; left: 32px; top: 84px;
    font-family: "DM Serif Display", serif; font-weight: 400;
    font-size: 37px; line-height: 46px; color: var(--ink); letter-spacing: -0.3px;
  }
  .chapter-body { position: absolute; left: 34px; top: 158px; width: 326px; }
  .chapter-body p {
    font-size: 9.5px; line-height: 11.5px; letter-spacing: 1.15px;
    color: var(--body-text); margin-bottom: 11px;
    hyphens: auto;
  }
  .chapter-body p.section-start { margin-top: 35px; }

  .playback { position: absolute; left: 0; top: 578px; width: 100%; height: 40px; }
  .playback svg { position: absolute; top: 0; }
</style>
</head>
<body>

<section class="screen screen--cover">
  <div class="cover-photo" role="img" aria-label="Cover photograph: a young man in a white t-shirt looking out over misty mountains under a cloudy dusk sky"></div>
  <svg class="icon cover-menu" width="20" height="18" viewBox="0 0 20 18" aria-label="Menu">
    <rect x="1" y="2" width="18" height="3" fill="var(--on-photo)"/>
    <rect x="1" y="8" width="18" height="3" fill="var(--on-photo)"/>
    <rect x="1" y="14" width="18" height="3" fill="var(--on-photo)"/>
  </svg>
  <svg class="icon cover-sound" width="22" height="22" viewBox="0 0 22 22" aria-label="Audio">
    <path d="M3 8h4l5-4v14l-5-4H3z" fill="none" stroke="var(--on-photo)" stroke-width="1.3" stroke-linejoin="round"/>
    <path d="M15 8c1.2 1.6 1.2 4.4 0 6" fill="none" stroke="var(--on-photo)" stroke-width="1.3" stroke-linecap="round"/>
    <path d="M17.5 5.5c2.4 3 2.4 8 0 11" fill="none" stroke="var(--on-photo)" stroke-width="1.3" stroke-linecap="round"/>
  </svg>
  <div class="cover-text">
    <p class="cover-author">Adrian Hale</p>
    <h1 class="cover-title">How to Be Yourself<br>&amp; Be Happy<br>With Your Life</h1>
  </div>
  <button class="read-button">READ</button>
</section>

<section class="screen screen--chapter">
  <svg class="icon chapter-menu" width="18" height="16" viewBox="0 0 18 16" aria-label="Menu">
    <rect x="1" y="1" width="16" height="3" fill="var(--icon-dark)"/>
    <rect x="1" y="7" width="16" height="3" fill="var(--icon-dark)"/>
    <rect x="1" y="13" width="16" height="3" fill="var(--icon-dark)"/>
  </svg>
  <svg class="icon chapter-next" width="26" height="18" viewBox="0 0 26 18" aria-label="Next page">
    <path d="M2 9h21M16 2l7 7-7 7" fill="none" stroke="var(--icon-dark)" stroke-width="1.4" stroke-linecap="round" stroke-linejoin="round"/>
  </svg>
  <h2 class="chapter-title">Chapter One</h2>
  <div class="chapter-body">
    <p>Lorem ipsum dolor sit amet, corpora consequat eos et, ex euismod feugait his. Cu movet verear interpretaris nec, te vel nisl volumus. Feugiat percipit mediocritatem sea ex. At qui ludus noster. Assum integre ut usu.</p>
    <p class="section-start">Sanctus eleifend at his, deseruisse persequeris in sit. Id quo dictas repudiare deseruisse, facete utroque ei pri. Cum ei affert salutandi moderatius, eu vero antiopam dignissim eam. Ius enim labitur signiferumque te, id nisl dico facilis sed, sed justo cotidieque ne. Mei elit corrumpit et, periculis suscipiantur quo ex. Id denique ponderum expetenda sed. Ut feugiat deleniti qui, vidit oporteat elaboraret eam at.</p>
    <p>Lorem ipsum dolor sit amet, corpora consequat eos et, ex euismod feugait his. Cu movet verear interpretaris nec, te vel nisl volumus. Feugiat percipit mediocritatem sea ex. At qui ludus noster. Assum integre ut usu.</p>
    <p>Sanctus eleifend at his, deseruisse persequeris in sit. Id quo dictas repudiare deseruisse, facete utroque ei pri.</p>
    <p>Cum ei affert salutandi moderatius, eu vero antiopam dignissim eam. Ius enim labitur signiferumque te, id nisl dico facilis sed, sed justo cotidieque ne. Mei elit corrumpit et, periculis suscipiantur quo ex. Id denique ponderum expetenda sed. Ut feugiat deleniti qui, vidit oporteat elaboraret eam at.</p>
  </div>
  <div class="playback">
    <svg style="left:72px;top:10px" width="28" height="20" viewBox="0 0 28 20" aria-label="Previous chapter">
      <path d="M14 1v18L2 10zM27 1v18L15 10z" fill="var(--control-grey)"/>
    </svg>
    <svg style="left:181px" width="34" height="38" viewBox="0 0 34 38" aria-label="Play">
      <path d="M3 1l30 18L3 37z" fill="var(--control-grey)"/>
    </svg>
    <svg style="left:289px;top:10px" width="28" height="20" viewBox="0 0 28 20" aria-label="Next chapter">
      <path d="M1 1v18l12-9zM14 1v18l12-9z" fill="var(--control-grey)"/>
    </svg>
  </div>
</section>

</body>
</html>
```